Website Redesign Project Puzzle Vault Leesburg

We are an escape room company located in Ashburn, Virginia. We currently have a website https://www.puzzlevaultleesburg.example based upon html/bootstrap/javascript/php/mysql and I'd like to keep it that way. I'm looking for someone upgrade the front page so it is more informative, cleaner, quicker to load, and optimizes the space for full sale opportunities.

Target Market(s)

Corporate Clients, Families, Friends. All ages

Industry/Entity Type

Entertainment Industry

Coding

Font styles to use
Other font styles liked:
• Similar to Facebook or Amazon

Requirements
Must have
• Must be mobile friendly. bootstrap. Lots of graphics (will provide) nice and easy to read fonts. Easy to read layout. Must look clean, fresh, exciting, and want to grab attention.
• Please visit my facebook page and website for more details. facebook.com/puzzlevaultleesburg
Nice to have
• Same color as existing but open to options if they look nice.
Should not have
• Should not be wordpress or hard to modify.

```html
<!DOCTYPE html>
<html lang="en">
<head>
<meta charset="utf-8">
<title>Puzzle Vault Leesburg</title>
<link href="https://fonts.googleapis.com/css2?family=Rajdhani:wght@600;700&family=Open+Sans:wght@400;600&display=swap" rel="stylesheet">
<style>
:root{
  --blue:#1a9be8;
  --blue-dark:#168ad0;
  --ink:#222;
  --card-dark:#3a3a3c;
  --black:#000;
  --footer:#111;
  --white:#fff;
  --grey-line:#bbb;
}
*{box-sizing:border-box;margin:0;padding:0}
html,body{width:1200px;height:3484px;overflow:hidden;background:var(--white)}
body{position:relative;font-family:"Open Sans",Arial,sans-serif;color:var(--ink)}
.abs{position:absolute}
.head{font-family:"Rajdhani","Arial Narrow",sans-serif;font-weight:700;text-transform:uppercase}

/* hero */
.hero{left:0;top:0;width:1200px;height:697px;background:radial-gradient(ellipse at 50% 40%,#5a2a2e 0%,#2a1620 45%,#120c16 100%)}
.hero-shade{left:0;top:0;width:1200px;height:697px;background:linear-gradient(90deg,rgba(120,10,20,.35),rgba(0,0,0,0) 40%,rgba(0,0,0,0) 60%,rgba(30,30,90,.35))}
.nav{top:56px;font-family:"Rajdhani",sans-serif;font-weight:700;font-size:16px;color:var(--white);letter-spacing:.2px}
.nav a{color:inherit;text-decoration:none;margin-right:18px}
.nav a.active{color:var(--blue)}
.brand{left:483px;top:22px;width:210px;height:134px;display:flex;align-items:center;gap:10px}
.brand-mark{width:44px;height:44px;background:var(--blue);flex:none}
.brand-name{font-family:"Rajdhani",sans-serif;font-weight:700;font-size:30px;line-height:30px;color:var(--blue);text-transform:uppercase}
.welcome{left:0;width:1200px;top:292px;text-align:center;font-size:48px;color:var(--blue)}
.hero-title{left:0;width:1200px;top:335px;text-align:center;font-size:88px;color:var(--white);line-height:100px}
.arrow{top:336px;width:52px;height:52px;border-radius:50%;background:rgba(140,140,150,.75)}

/* room cards */
.card{top:754px;width:224px;height:364px;color:var(--white);text-align:center;border:1px solid #ddd}
.card.blue{background:var(--blue)}
.card.dark{background:var(--card-dark)}
.card-img{height:168px;width:100%}
.card h3{font-size:20px;margin-top:16px}
.card .diff{font-size:15px;margin-top:8px}
.card p{font-size:11.5px;line-height:17px;margin:4px 14px 0}

/* corporate */
.corp{left:0;top:1187px;width:1200px;height:645px;background:linear-gradient(135deg,#3a3634,#24211f 50%,#34302e)}
.corp-title{left:0;width:1200px;top:1235px;text-align:center;font-size:38px;color:var(--white)}
.corp-item{left:192px;width:440px;color:var(--white)}
.corp-item h4{font-size:20px;margin-bottom:6px}
.corp-item p{font-size:13px;line-height:19.5px}
.corp-form{left:725px;top:1329px;width:328px;height:403px;background:var(--black);padding:34px 26px 0}
.field{height:40px;border:1px solid #666;font-size:14px;padding:10px 14px;margin-bottom:8px;color:var(--white)}
.corp-form .field.tall{height:88px}
.btn{height:42px;background:var(--blue);color:var(--white);font-weight:600;text-align:center;font-size:16px;line-height:42px;margin-top:14px}

/* birthday */
.bday-title{left:196px;top:1924px;font-size:36px;color:var(--ink)}
.bday-text{left:197px;top:1982px;width:520px;font-size:15.5px;line-height:23px;color:#444}
.option{left:196px;width:490px;height:76px;color:var(--white);font-size:15.5px;line-height:23px;padding:15px 60px 0 18px}
.option svg{position:absolute;right:14px;top:24px}
.opt-blue{background:var(--blue);top:2113px}
.opt-dark{background:var(--card-dark);top:2209px}
.note{left:201px;top:2307px;width:420px;font-size:15px;line-height:23px;color:#333}
.bday-form{left:732px;top:1919px;width:329px;height:405px;border:3px solid #e8e8e8;background:var(--white);padding:32px 26px 0}
.bday-form .field{color:#333;border-color:#999;height:40px;margin-bottom:8px}
.bday-form .field.tall{height:88px}
.row{display:flex;gap:6px}
.row .field{flex:1}

/* how it works */
.how{left:0;top:2430px;width:1200px;height:506px;background:var(--blue);color:var(--white)}
.how-title{left:0;width:1200px;top:2500px;text-align:center;font-size:38px}
.how-intro{left:190px;width:820px;top:2561px;text-align:center;font-size:14px;line-height:20px}
.faq{width:370px;font-family:"Rajdhani",sans-serif;font-weight:700;font-size:18px;color:var(--white)}
.faq .q{height:38.5px;display:flex;justify-content:space-between}
.faq .a{font-family:"Open Sans",sans-serif;font-weight:400;font-size:14px;line-height:20px;margin:-14px 0 2px;opacity:.9}

/* contact */
.contact{left:0;top:2936px;width:1200px;height:460px;background:var(--black);color:var(--white)}
.contact-title{left:0;width:1200px;top:2990px;text-align:center;font-size:38px;color:var(--white)}
.info{color:var(--white)}
.info h5{font-family:"Rajdhani",sans-serif;font-weight:700;font-size:20px}
.info p{font-size:18.5px;line-height:28px}
.info svg{position:absolute;left:-54px;top:2px}
.footer{left:0;top:3396px;width:1200px;height:88px;background:var(--footer)}
.copy{left:198px;top:3427px;font-size:13px;color:#aaa}
.social{top:3424px;left:830px;display:flex;gap:22px;font-size:13px;font-weight:600;color:var(--blue)}
</style>
</head>
<body>

<section>
  <div class="abs hero" role="img" aria-label="Photo of a smiling group of players posing inside a red-lit escape room"></div>
  <div class="abs hero-shade"></div>
  <nav class="abs nav" style="left:118px"><a class="active" href="#">HOME</a><a href="#">ESCAPE ROOMS</a><a href="#">SPECIAL EVENTS</a></nav>
  <nav class="abs nav" style="left:737px"><a href="#">LOCATIONS</a><a href="#">HOW IT WORKS</a><a href="#" style="margin-right:0">CONTACT US</a></nav>
  <div class="abs brand"><span class="brand-mark"></span><span class="brand-name">Puzzle Vault Leesburg</span></div>
  <h2 class="abs head welcome">Welcome to</h2>
  <h1 class="abs head hero-title">Escape Rooom</h1>
  <div class="abs arrow" style="left:130px"><svg width="52" height="52"><path d="M30 16 L20 26 L30 36" stroke="#222" stroke-width="3" fill="none"/></svg></div>
  <div class="abs arrow" style="left:1016px"><svg width="52" height="52"><path d="M22 16 L32 26 L22 36" stroke="#222" stroke-width="3" fill="none"/></svg></div>
</section>

<section>
  <div class="abs card blue" style="left:124px">
    <div class="card-img" role="img" aria-label="Photo of a folding elevator gate" style="background:linear-gradient(#8c8a86,#4a4642)"></div>
    <h3 class="head">Elevator</h3><div class="diff">Difficulty: 10/10</div>
    <p>The main elevators are down so you'll need to take the freight elevator to the top floor if you want to get your award. The last celebrity that attempted to do so wasn't so lucky.</p>
  </div>
  <div class="abs card dark" style="left:365px">
    <div class="card-img" role="img" aria-label="Photo of a colourful candy shop room" style="background:linear-gradient(#9a4a4a,#7a8aa8 50%,#e4ece8)"></div>
    <h3 class="head">Candy Shop</h3><div class="diff">Difficulty: 7/10</div>
    <p>With all of the candy right before your eyes, find the golden ticket and win the prize!</p>
  </div>
  <div class="abs card blue" style="left:605px">
    <div class="card-img" role="img" aria-label="Photo of a bank vault door" style="background:linear-gradient(90deg,#2a3038,#5a6068 70%,#c8ccd0)"></div>
    <h3 class="head">Bank Heist</h3><div class="diff">Difficulty: 8/10</div>
    <p>With your family held hostage, the mob gave you one choice - rob the bank in exchange for their freedom or its goodbyes forever.</p>
  </div>
  <div class="abs card dark" style="left:846px">
    <div class="card-img" role="img" aria-label="Photo of players in orange jumpsuits in a jail cell room" style="background:linear-gradient(#5a5c60,#d8502a 65%,#a83a20)"></div>
    <h3 class="head">Jail Break</h3><div class="diff">Difficulty: 8/10</div>
    <p>One Guard, One Goal: get out</p>
  </div>
</section>

<section>
  <div class="abs corp" role="img" aria-label="Photo of a large corporate group posing in the escape room lobby, darkened"></div>
  <h2 class="abs head corp-title">Corporate Events</h2>
  <div class="abs corp-item" style="top:1344px"><h4 class="head">On-site multi-room</h4><p>Come, enjoy, relax in our multi-room escape room facility with your team. With four different rooms to choose from we are able to accommodate up to 30 people in a single hour.</p></div>
  <div class="abs corp-item" style="top:1475px"><h4 class="head">Off-site hot seat escape room package</h4><p>Enjoy a 2 or 4 hour escape room in the new thrilling Hot Seat challenge! Each player is given two minutes to solve the challenge at hand before they go up in smoke! Can you do it?<br>Number of Players: 20 to 100</p></div>
  <div class="abs corp-item" style="top:1623px"><h4 class="head">Off-site custom escape room package</h4><p>Enjoy a customized escape room game to fit the theme you'd like to celebrate. You and your team will come in to work or what seems to be a normal work day until they arrive in an immersive experience for all to enjoy. Each game is customized and includes live actors.</p></div>
  <form class="abs corp-form">
    <div class="field">Name</div><div class="field">Select Package</div><div class="field">Phone</div><div class="field">Email</div>
    <div class="field tall">Description</div>
    <div class="btn">SUBMIT</div>
  </form>
</section>

<section>
  <h2 class="abs head bday-title">Birthday Parties</h2>
  <p class="abs bday-text">Celebrate this year in style by treating your family with an escape room birthday package. You and your loved ones have the choice of four escape rooms and will enjoy a private party afterwards in our party room. Either of these packages will be sure to satisfy your needs.</p>
  <div class="abs option opt-blue">A private escape room event with party room pizza and soda. Add just $150 to your escape room.<svg width="18" height="30"><path d="M3 3 L15 15 L3 27" stroke="#fff" stroke-width="2" fill="none"/></svg></div>
  <div class="abs option opt-dark">A private escape room event with a party room rental. Bring your own food. Add just $125.<svg width="18" height="30"><path d="M3 3 L15 15 L3 27" stroke="#fff" stroke-width="2" fill="none"/></svg></div>
  <p class="abs note">Note: A $50 cleaning fee applies to all parties who don't clean after themselves</p>
  <form class="abs bday-form">
    <div class="field">Name</div>
    <div class="row"><div class="field">Number</div><div class="field">Group size</div></div>
    <div class="field">Package</div><div class="field">Email</div>
    <div class="field tall">Description</div>
    <div class="btn">SUBMIT</div>
  </form>
</section>

<section>
  <div class="abs how"></div>
  <h2 class="abs head how-title" style="color:var(--white)">How it works</h2>
  <p class="abs how-intro" style="color:var(--white)">An escape room is a themed environment where you and your friends must work together to complete the objectives through solving puzzles before time runs out. Most missions will lock you in while some of our missions do not.</p>
  <div class="abs faq" style="left:199px;top:2643px">
    <div class="q"><span>How do I make a reservation?</span><span>+</span></div>
    <div class="a">Click on the Book now button or<br>click here Book Now.</div>
    <div class="q"><span>I'm pregnant, can I participate?</span><span>+</span></div>
    <div class="q"><span>Do I have to sign a liability waiver?</span><span>+</span></div>
    <div class="q"><span>What time should we arrive?</span><span>+</span></div>
  </div>
  <div class="abs faq" style="left:617px;top:2643px;width:400px">
    <div class="q"><span>How long does an escape last?</span><span>+</span></div>
    <div class="q"><span>How can I redeem a voucher or promo code?</span><span>+</span></div>
    <div class="q"><span>Which room is the most challenging?</span><span>+</span></div>
    <div class="q"><span>Is there an age limit?</span><span>+</span></div>
    <div class="q"><span>Where do I park?</span><span>+</span></div>
  </div>
</section>

<section>
  <div class="abs contact"></div>
  <h2 class="abs head contact-title">Contact Us</h2>
  <div class="abs info" style="left:255px;top:3076px">
    <svg width="44" height="44" viewBox="0 0 44 44"><path d="M10 4 L17 4 L20 13 L15 17 C18 24 21 27 28 30 L32 25 L41 28 L41 35 C41 38 38 41 34 40 C18 37 7 26 4 10 C3 6 6 4 10 4 Z" fill="none" stroke="#1a9be8" stroke-width="2.5"/></svg>
    <h5>PHONE</h5><p>(571) 555 0148</p>
  </div>
  <div class="abs info" style="left:710px;top:3076px">
    <svg width="46" height="40" viewBox="0 0 46 40" style="left:-61px"><rect x="2" y="4" width="42" height="32" rx="3" fill="none" stroke="#1a9be8" stroke-width="2.5"/><path d="M3 6 L23 22 L43 6" fill="none" stroke="#1a9be8" stroke-width="2.5"/></svg>
    <h5>EMAIL</h5><p>sales@puzzlevaultleesburg.example</p>
  </div>
  <div class="abs info" style="left:259px;top:3192px">
    <svg width="40" height="52" viewBox="0 0 40 52" style="left:-56px"><path d="M20 49 C10 34 4 26 4 18 A16 16 0 0 1 36 18 C36 26 30 34 20 49 Z" fill="none" stroke="#1a9be8" stroke-width="2.5"/><circle cx="20" cy="18" r="6" fill="none" stroke="#1a9be8" stroke-width="2.5"/></svg>
    <h5>ADDRESSS</h5><p>1570 Harbor Mill Lane,<br>Suite 12, Leesburg, Va 20175</p>
  </div>
  <div class="abs info" style="left:710px;top:3192px">
    <svg width="50" height="50" viewBox="0 0 50 50" style="left:-62px"><circle cx="25" cy="25" r="22" fill="none" stroke="#1a9be8" stroke-width="2.5"/><circle cx="25" cy="25" r="15" fill="none" stroke="#1a9be8" stroke-width="2"/><path d="M25 15 L25 26 L32 26" fill="none" stroke="#1a9be8" stroke-width="2.5"/></svg>
    <h5>HOURS</h5><p>Wednesday - Fridays (4 to 10pm)<br>Weekends (11am to 9pm).</p>
  </div>
  <div class="abs footer"></div>
  <p class="abs copy">© 2019 Company Name &nbsp;All right reserved</p>
  <div class="abs social"><span>Share</span><span>Follow</span><span>Connect</span><span>Photos</span></div>
</section>

</body>
</html>
```